Wordpress design for my private practice website - Psychotherapist

I would like a simple, clean, and elegant design for my private practice website. I work with both adults and children so I'd like it to appeal to both. However, since parents make the choice as to where to send their child for therapy, I want it to appeal to adults more. I would like the pictures on the site to have a calming effect - maybe using sand and water and rocks. I am attaching files with my company logo. I would also like my name incorporated into the header - Colette Brannigan, LCSW, Registered Play Therapist. I've also uploaded a picture of myself for my About Page.

I like the design of these 2 website and want something similar:
www.drlorapenwick.example
www.harwood-tallis.example

I would like a home page that highlights a calming graphic across the entire top of the page as well as my practice logo and my name.

I'd like a link to social media sites on the top of the homepage - facebook, pinterest.

I want a simple bar across the top with the following tabs:
Home
About Me (subtabs Who I Am, Specialties and Approach)
Counseling Services (subtabs Individual Counseling, Play Therapy, Sandplay Therapy,)
Fees
FAQs
Contact Me (would love this to be a fill in the blank contact form that sends info to my email address - should include name, phone number, email and a comment box for more information requested)
Blog (this will link with another wordpress blog)

Target Market(s)

Parents of children under age 12 with behavioral problems or are dealing with the breakup of their family through divorce - looking for someone to work with their young child. I also work with Adults that are overwhelmed and worried - often women that have many life stressors and are feeling burnt out on life and meeting everyone's needs. Families going through some type of trauma, including divorce or grief work. I also work with individuals going through a transition of religious beliefs - often exiting the religion of their youth and undergoing a crisis of faith at midlife.

Industry/Entity Type

Mental Health

Contact Information for Business Card

Colette Brannigan, LCSW
Registered Play Therapist
4917 Wexmoor Lane
Idaho Falls, Idaho 83404
(208)555-0187
www.stillbrookcounseling.example

On the opposite side, I'd like an appointment reminder area - with the following text:

Your next appointment is
_____/______/______ at ______am/pm
Please give 24 hrs notice if you need to cancel your appointment.

Coding

Coded - Design and coding required

Number of Pages Required

5+ page

Font styles to use
Sans Serif

Colors
33a6d7
9bcb3c
0355a3

Requirements
Must have
• I'd like it to be a wordpress site. I'm such a newby at web design - but I need to be able to add content and manage the site myself once it is up and running.
Nice to have
• I like the design of these 2 websites and want something similar:
• www.drlorapenwick.example
• www.harwood-tallis.example
• They are clean, easy to navigate and calming.
Should not have
• Should not look like a childcare website.

```html
<!DOCTYPE html>
<html lang="en">
<head>
<meta charset="utf-8">
<title>Stillbrook Counseling – Colette Brannigan</title>
<link rel="stylesheet" href="https://fonts.googleapis.com/css2?family=Arimo:ital,wght@0,400;0,700;1,400&family=Noto+Sans:ital,wght@0,400;0,700;1,400&display=swap">
<style>
  :root {
    --ink: #1a1a1a;
    --text: #5b5b5b;
    --muted: #8a8a8a;
    --accent: #1b7fb3;
    --footer: #1b87b5;
    --white: #ffffff;
    --hero-deep: #0f3a44;
    --hero-mid: #3d7f8c;
    --hero-light: #9cc8cf;
  }
  * { box-sizing: border-box; margin: 0; padding: 0; }
  html, body { width: 1200px; height: 2276px; overflow: hidden; background: var(--white); }
  body { position: relative; font-family: "Noto Sans", Verdana, sans-serif; color: var(--text); }
  a { color: inherit; text-decoration: none; }

  /* Hero */
  .hero {
    position: absolute; left: 0; top: 0; width: 1200px; height: 535px;
    background:
      radial-gradient(ellipse 380px 260px at 780px 160px, rgba(190,225,230,.55), transparent 70%),
      radial-gradient(ellipse 500px 300px at 1050px 420px, rgba(40,90,100,.6), transparent 70%),
      linear-gradient(135deg, var(--hero-mid) 0%, var(--hero-deep) 45%, var(--hero-mid) 70%, var(--hero-light) 100%);
  }
  .nav { position: absolute; top: 30px; left: 0; width: 1200px; height: 22px; font-family: "Arimo", Arial, sans-serif; font-weight: 700; font-size: 13px; color: var(--white); }
  .nav a, .nav span { position: absolute; top: 0; line-height: 22px; }
  .nav .brand { left: 98px; font-size: 10px; }
  .social { position: absolute; width: 16px; height: 16px; border-radius: 50%; background: var(--white); top: 3px; }
  .nav .social { top: 3px; }
  .nav .contact-link { left: 972px; color: var(--ink); }

  .hero-title { position: absolute; left: 98px; top: 163px; font-family: "Arimo", Arial, sans-serif; font-weight: 700; font-size: 52px; color: var(--white); letter-spacing: .5px; }
  .hero-rule { position: absolute; left: 100px; top: 240px; width: 488px; height: 3px; background: var(--white); }
  .hero-name { position: absolute; left: 100px; top: 265px; font-family: "Arimo", Arial, sans-serif; font-style: italic; font-size: 24px; color: var(--white); }
  .hero-role { position: absolute; left: 100px; top: 306px; font-family: "Arimo", Arial, sans-serif; font-style: italic; font-size: 18px; color: var(--white); }
  .hero-button { position: absolute; left: 98px; top: 358px; width: 150px; height: 47px; border: 3px solid var(--white); background: rgba(10,40,50,.35); color: var(--white); font-weight: 700; font-size: 18px; text-align: center; line-height: 41px; }

  /* About */
  .section-title { position: absolute; left: 0; width: 1200px; text-align: center; font-weight: 700; font-size: 36px; color: var(--ink); }
  .about-title { top: 592px; }
  .about-intro { position: absolute; left: 385px; top: 674px; width: 430px; text-align: center; font-size: 13px; line-height: 20px; color: var(--text); }
  .service { position: absolute; top: 780px; width: 200px; text-align: center; }
  .service svg { display: block; margin: 0 auto; }
  .service-label { display: block; margin-top: 20px; font-size: 12px; font-weight: 700; color: var(--ink); }

  .photo { position: absolute; top: 958px; height: 208px; }
  .photo-lake { left: 98px; width: 332px; background: linear-gradient(180deg, #3f8fd6 0%, #9ac6e6 28%, #7a8a6e 45%, #2aa3b5 60%, #0d6f8a 100%); }
  .photo-hands { left: 434px; width: 332px; background: linear-gradient(120deg, #5fb1e0 0%, #e9c36a 30%, #d84a3e 50%, #c9a38a 70%, #f0e3d4 100%); }
  .photo-sand { left: 770px; width: 333px; background: linear-gradient(135deg, #e6e2dc 0%, #cfc9c1 50%, #bdb6ad 100%); }

  .post { position: absolute; top: 1215px; width: 250px; text-align: center; }
  .post-meta { font-family: "Arimo", Arial, sans-serif; font-style: italic; font-size: 10px; color: var(--muted); }
  .post-title { margin-top: 16px; font-size: 16px; font-weight: 700; line-height: 21px; color: var(--ink); }
  .post-body { margin-top: 16px; font-size: 13px; line-height: 20px; color: var(--text); }

  .blog-button { position: absolute; left: 553px; top: 1428px; width: 94px; height: 28px; border: 2px solid var(--accent); color: var(--accent); font-size: 13px; font-weight: 700; text-align: center; line-height: 24px; }

  .banner { position: absolute; left: 0; top: 1512px; width: 1200px; height: 270px;
    background:
      radial-gradient(ellipse 220px 160px at 870px 140px, rgba(60,40,35,.55), transparent 70%),
      radial-gradient(ellipse 380px 220px at 700px 130px, rgba(240,250,250,.75), transparent 70%),
      linear-gradient(90deg, #56b6ad 0%, #8fd0c6 35%, #bfe2e0 60%, #8ccbc8 100%); }

  /* FAQ */
  .faq-title { position: absolute; left: 262px; top: 1848px; font-size: 24px; font-weight: 700; color: var(--ink); letter-spacing: 1px; }
  .faq { position: absolute; top: 1914px; width: 290px; }
  .faq-q { font-family: "Arimo", Arial, sans-serif; font-style: italic; font-size: 13.5px; line-height: 20px; color: var(--muted); }
  .faq-a { margin-top: 22px; font-size: 13px; line-height: 20px; color: var(--text); }
  .faq-more { position: absolute; left: 0; top: 2074px; width: 1200px; text-align: center; font-size: 14px; font-weight: 700; color: var(--accent); }

  /* Footer */
  .footer { position: absolute; left: 0; top: 2163px; width: 1200px; height: 113px; background: var(--footer); font-family: "Arimo", Arial, sans-serif; font-weight: 700; font-size: 14px; color: var(--white); }
  .footer a { position: absolute; top: 46px; line-height: 20px; }
  .footer .social { top: 48px; }
</style>
</head>
<body>
  <header class="hero" role="img" aria-label="Close-up photograph of water droplets on a teal feather">
    <nav class="nav">
      <span class="brand">Stillbrook</span>
      <a style="left:160px">About me</a>
      <a style="left:253px">Counselling Services</a>
      <a style="left:413px">Fees</a>
      <a style="left:471px">FAQ`S</a>
      <a class="contact-link">Contact me</a>
      <span class="social" style="left:1060px" aria-label="Social profile link"></span>
      <span class="social" style="left:1086px" aria-label="Social profile link"></span>
    </nav>
    <h1 class="hero-title">STILLBROOK</h1>
    <div class="hero-rule"></div>
    <p class="hero-name">Colette Brannigan</p>
    <p class="hero-role">LCSW, Registered Play Therapist</p>
    <a class="hero-button">CONTACT ME</a>
  </header>

  <main>
    <h2 class="section-title about-title">ABOUT ME</h2>
    <p class="about-intro">Lorem ipsum dolor sit amet, consectetur adipiscing elit. Donec sodales mi id augue fermentum maximus. Vivamus feugiat odio nec enim lobortis tempor at sit amet neque</p>

    <div class="service" style="left:323px">
      <svg width="70" height="70" viewBox="0 0 70 70" fill="none" stroke="#1b7fb3" stroke-width="2.5" stroke-linejoin="round">
        <path d="M8 20h14a6 6 0 1 1 12 0h14v14a6 6 0 1 0 0 12v14H34a6 6 0 1 0-12 0H8V46a6 6 0 1 1 0-12z"/>
      </svg>
      <span class="service-label">individual counseling</span>
    </div>
    <div class="service" style="left:501px">
      <svg width="70" height="70" viewBox="0 0 70 70" fill="none" stroke="#1b7fb3" stroke-width="2.5" stroke-linejoin="round" stroke-linecap="round">
        <path d="M62 6C45 8 32 18 24 34l12 12c16-8 26-21 28-38z"/>
        <circle cx="44" cy="26" r="5"/>
        <path d="M24 34l-12 2-6 8 12 2M36 46l-2 12-8 6-2-12"/>
        <path d="M18 50l-10 12M22 54l-6 8"/>
      </svg>
      <span class="service-label">play therapy</span>
    </div>
    <div class="service" style="left:683px">
      <svg width="70" height="70" viewBox="0 0 70 70" fill="none" stroke="#1b7fb3" stroke-width="2.5" stroke-linecap="round">
        <ellipse cx="35" cy="14" rx="9" ry="6"/>
        <ellipse cx="35" cy="34" rx="20" ry="8"/>
        <ellipse cx="35" cy="56" rx="28" ry="10"/>
      </svg>
      <span class="service-label">sandplay therapy</span>
    </div>

    <div class="photo photo-lake" role="img" aria-label="Photograph of smooth boulders in clear blue lake water"></div>
    <div class="photo photo-hands" role="img" aria-label="Photograph of paint-covered hands forming a heart"></div>
    <div class="photo photo-sand" role="img" aria-label="Photograph of grey stones in raked sand ripples"></div>

    <article class="post" style="left:139px">
      <p class="post-meta">22 February 2016 | individual counseling</p>
      <h3 class="post-title">Lorem ipsum dolor sit amet, consectetur adipiscing elit</h3>
      <p class="post-body">Nec enim lobortis tempor at sit amet neque. Mauris ac ultricies massa. Nullam vel nisl erat. Aliquam condimentum</p>
    </article>
    <article class="post" style="left:476px">
      <p class="post-meta">22 February 2016 | individual counseling</p>
      <h3 class="post-title">Lorem ipsum dolor sit amet, consectetur adipiscing elit</h3>
      <p class="post-body">Vivamus feugiat odio nec enim lobortis tempor at sit amet neque. Mauris ac ultricies massa. Nullam vel nisl erat. Aliquam condimentum</p>
    </article>
    <article class="post" style="left:811px">
      <p class="post-meta">22 February 2016 | individual counseling</p>
      <h3 class="post-title">Lorem ipsum dolor sit amet, consectetur adipiscing elit</h3>
      <p class="post-body">Vivamus feugiat odio nec enim lobortis tempor at sit amet neque. Mauris ac ultricies massa</p>
    </article>

    <a class="blog-button">BLOG</a>

    <div class="banner" role="img" aria-label="Close-up photograph of a dandelion seed head on a soft teal background"></div>

    <h2 class="faq-title">FAQ`S</h2>
    <div class="faq" style="left:263px">
      <p class="faq-q">Vivamus feugiat odio nec enim lobortis tempor at sit amet neque?</p>
      <p class="faq-a">Vivamus feugiat odio nec enim lobortis tempor at sit amet neque. Mauris ac ultricies massa. Nullam vel nisl erat. Aliquam condimentum</p>
    </div>
    <div class="faq" style="left:643px">
      <p class="faq-q">Vivamus feugiat odio nec enim lobortis tempor at sit amet neque?</p>
      <p class="faq-a">Vivamus feugiat odio nec enim lobortis tempor at sit amet neque. Mauris ac ultricies massa. Nullam vel nisl erat. Aliquam condimentum</p>
    </div>
    <a class="faq-more">MORE</a>
  </main>

  <footer class="footer">
    <a style="left:100px">About me</a>
    <a style="left:205px">Counselling Services</a>
    <a style="left:386px">Fees</a>
    <a style="left:453px">FAQ`S</a>
    <a style="left:527px">Contact me</a>
    <span class="social" style="left:1060px" aria-label="Social profile link"></span>
    <span class="social" style="left:1087px" aria-label="Social profile link"></span>
  </footer>
</body>
</html>
```